Design for landing page for startup within book publishing and book sales connected to NFT

This is a website design job, not a web development job.
Specification in words
A one page landingpage to market a NFT project. This is a marketing page that has the purpose of building a community and attracting investors. This job is ONLY design in Figma for landing page.

It is for a NFT based project but the idea concerns publishing of books, selling of books and games around books.

The name is quillora.

Check the site vantrel.co, it is going to be a bit of that concept. Vantrel is music but this is going to be free reading of books.

A simple (clean minimalistic design) is preferable.

The design specification below gives you an idea of how we want that to look.

Also in complement with the design spec then if possible throw in a bit of gaming feeling and also a bit of metaverse feeling.

Give a feeling that attracts authors (not too "NFT like") but still get some feeling of NFT innovation and a bit metaverse.

Mobile responsive.

Parts of page
Menulevel: Logo, Connection to Chirpna, Gathrix, Scrivo, Wiremoss. Join Waitlist.

Banner explaining the concept.

Banner to join waitlist with button.

Part with description of features including some "screenshots" of browsing books (like browsing movies in KLV plex).

Team.

Roadmap.

FAQ.

White paper.

Specification in design

Minimalistic, modern looking. Gradient and shadings if possible. Basically some kind of version of KLV plex is what I see before my eyes. Try to combine Borvex with KLV plex. KLV plex is a movie site but the design is superior to Borvex.

For colors, use the color scale of the Zodiac sign Leo. This is an example: https://starguide.example-tally.com/astrology-signs-personality/leo-colors-palettes-help-you-shine

https://www.plumcosmos.co/love/leo-Leo-Color-Characteristics-and-Love-19.html

Gold and purple should be the dominant colors:
https://www.orbwisp.com/zodiac-signs/leo

The colors like this but less aggressive:
​​https://pellarcrane.movie/

Try to make a good UX/UI design also so that the users easy can interact with the interface.
Updates

Scope of project changed from 5 to 1 page.

As an answer to a question I got: This project is for design only. Nothing else.

Promonged on the request of designers.

Target Market(s)

Book publishing and book purchasing. NFT.

Industry/Entity Type

Book publishing. Book purchase. NFT.

Number of Pages Required

1 page

Font styles to use
Sans Serif

Colors
FFF300
FFF600
FEFA6F
FFFEC7
FFFEE8
FFC000
F8CF3A
FAE287
FDF2CF
FEFAEE
F0912C
F2A743
F7CA91
FBE8D2
FDF5EE
EE7325
F08F49
F5BC92
FAE3D3
FDF4ED
EB3D1F
EC4F4E
F09395
F8D3D4
FCEDEE
E54698
E96AAD
F1A4CE
F9D9EA
FCEFF6
A7469A
B969AE
D3A5CF
EDDBEB
F8F0F9
6B429C
8869AF
B7A5CE
E3DAEB
F3F0F8

Requirements
Must have
• A design that astonishes the users :-).
Nice to have
• Some innovative design.

```html
<!DOCTYPE html>
<html lang="en">
<head>
<meta charset="utf-8">
<title>Quillora — Read, collect and publish books</title>
<link rel="stylesheet" href="https://fonts.googleapis.com/css2?family=League+Spartan:wght@400;500;600;700&family=Arimo:wght@400;700&display=swap">
<style>
:root{
  --night:#22154a;
  --night-deep:#150b30;
  --header:#231650;
  --gold:#FFC000;
  --gold-soft:#F8CF3A;
  --orange:#F0912C;
  --red:#EB3D1F;
  --pink:#E54698;
  --magenta:#A7469A;
  --violet:#6B429C;
  --blue:#1a8ed0;
  --grey:#8e8e98;
  --white:#ffffff;
  --ink:#2b2440;
  --muted:#6b6680;
  --head:"League Spartan",sans-serif;
  --body:"Arimo",sans-serif;
}
*{box-sizing:border-box;margin:0;padding:0}
html,body{width:1200px;height:4644px;overflow:hidden}
body{background:var(--night);font-family:var(--body);color:var(--white);position:relative}
.page{position:relative;width:1200px;height:4644px;overflow:hidden}
.abs{position:absolute}
a{color:inherit;text-decoration:none}
.grad-btn{display:flex;align-items:center;justify-content:center;border-radius:40px;background:linear-gradient(90deg,var(--gold),var(--orange) 45%,var(--red) 75%,var(--pink));font-family:var(--head);color:var(--ink);font-weight:500}
.section-title{position:absolute;left:0;width:1200px;text-align:center;font-family:var(--head);font-weight:600;font-size:42px;color:var(--white)}

/* header */
.site-header{left:0;top:0;width:1200px;height:114px;background:var(--header);border-bottom:1px solid rgba(255,255,255,.06)}
.brand{display:flex;align-items:center;gap:10px;font-family:var(--head);font-weight:700;color:var(--gold);font-size:38px}
.brand-dot{width:22px;height:22px;border-radius:50%;background:var(--gold)}
.connect{left:634px;top:47px;font-size:13px;color:#e8e4f5}
.social-circle{width:40px;height:40px;border:1.5px solid #fff;border-radius:50%;display:flex;align-items:center;justify-content:center;font-family:var(--head);font-size:12px;font-weight:600}
.header-cta{left:946px;top:36px;width:140px;height:40px;font-size:14px}

/* hero */
.hero-art{left:0;top:114px;width:1200px;height:690px;background:
  radial-gradient(circle at 72% 40%,rgba(233,106,173,.35),transparent 30%),
  radial-gradient(circle at 30% 70%,rgba(167,70,154,.6),transparent 35%),
  radial-gradient(circle at 85% 75%,rgba(26,142,208,.35),transparent 30%),
  linear-gradient(180deg,#1e1350 0%,#3a1a7a 55%,#6a1e9c 80%,#2b1262 100%)}
.hero-title{left:108px;top:306px;font-family:var(--head);font-weight:700;font-size:86px;line-height:1}
.hero-copy{left:110px;top:414px;width:420px;font-family:var(--head);font-size:15px;line-height:22px}
.hero-cta{left:112px;top:477px;width:140px;height:40px;font-size:14px}
.slider-dots{left:1130px;top:358px;width:70px}
.slider-dots .num{width:30px;height:30px;border-radius:50%;background:var(--orange);font-family:var(--head);font-weight:700;font-size:15px;display:flex;align-items:center;justify-content:center}
.slider-dots .line{position:absolute;left:30px;top:15px;width:40px;height:2px;background:var(--orange)}
.slider-dots .dot{position:absolute;left:9px;width:12px;height:12px;border-radius:50%;background:#fff}

/* books */
.book-card{width:227px;height:315px;background:#fff;border-radius:38px}
.book-cover{width:159px;height:222px;border-radius:4px}
.author{display:flex;align-items:center;gap:8px}
.author-avatar{width:38px;height:38px;border-radius:50%;background:linear-gradient(135deg,#c9a58c,#6d4c3d)}
.author-name{font-family:var(--head);font-size:16px;color:var(--ink)}
.author-role{font-family:var(--head);font-size:13px;color:var(--pink);font-weight:500}
.buy-btn{width:159px;height:46px;border-radius:30px;padding:2px;background:linear-gradient(90deg,var(--gold),var(--red),var(--pink))}
.buy-btn span{display:flex;width:100%;height:100%;border-radius:30px;background:#fff;align-items:center;justify-content:center;font-family:var(--head);font-size:16px;color:var(--ink)}
.more-btn{width:142px;height:43px;font-size:14px;font-weight:600}
.more-btn i{display:inline-block;width:12px;height:12px;border-radius:50%;background:var(--ink);margin-left:5px;position:relative}
.more-btn i::after{content:"";position:absolute;left:3px;top:3px;width:4px;height:4px;border-top:1.5px solid #fff;border-right:1.5px solid #fff;transform:rotate(45deg)}

/* team */
.member{width:240px;text-align:center}
.member-photo{width:234px;height:234px;border-radius:50%;margin:0 auto}
.member-name{font-family:var(--head);font-size:22px;font-weight:500;margin-top:20px}
.member-company{font-size:13px;margin-top:10px;color:#e1dcef}

/* roadmap */
.roadmap-band{left:0;top:2380px;width:1200px;height:820px;background:var(--night-deep)}
.roadmap-glow{left:0;top:2790px;width:1200px;height:290px;background:
  radial-gradient(ellipse at 30% 50%,rgba(167,70,154,.55),transparent 55%),
  radial-gradient(ellipse at 80% 60%,rgba(107,66,156,.6),transparent 55%),
  radial-gradient(ellipse at 55% 40%,rgba(26,142,208,.3),transparent 50%)}
.stage{height:86px;top:2766px;width:243px;display:flex;align-items:center}
.stage-icon{width:80px;height:80px;border-radius:50%;background:#fff;border:4px solid;display:flex;align-items:center;justify-content:center;margin-left:2px}
.stage-label{font-family:var(--head);font-size:18px;margin-left:18px}
.milestone-no{font-size:11px}
.milestone-text{width:200px;font-family:var(--head);font-size:13px;line-height:21px}
.milestone-line{width:2px}

/* papers */
.paper-card{top:3315px;width:312px;height:325px;border-radius:38px;overflow:hidden;background:#fff;text-align:center;color:var(--ink)}
.paper-card h3{font-family:var(--head);font-weight:500;font-size:21px;margin-top:66px}
.paper-card p{font-family:var(--head);font-size:13px;line-height:21px;color:var(--muted);margin:16px 34px 0}
.paper-card .learn{display:inline-block;margin-top:14px;font-family:var(--head);font-size:13px;font-weight:600;text-decoration:underline}
.paper-mesh{position:absolute;left:0;bottom:0;width:100%;height:140px;background:linear-gradient(180deg,#fff,#e4e4ea 60%,#d4d4dc)}
.paper-card::after{content:"";position:absolute;left:0;bottom:0;width:100%;height:4px;background:linear-gradient(90deg,var(--gold),var(--red),var(--pink))}

/* newsletter */
.newsletter{left:112px;top:3802px;width:976px;height:211px;background:var(--blue);border-radius:10px}
.newsletter h2{position:absolute;left:50px;top:42px;font-family:var(--head);font-weight:700;font-size:50px;line-height:58px}
.signup{position:absolute;left:448px;top:66px;width:478px;height:54px;background:#fff;border-radius:6px;display:flex;align-items:center;padding-left:24px;font-size:13px;color:#555}
.signup-btn{position:absolute;right:4px;top:4px;width:160px;height:46px;border-radius:6px;background:linear-gradient(90deg,var(--gold),var(--orange));display:flex;align-items:center;justify-content:center;font-family:var(--head);font-weight:700;font-size:14px;color:var(--red)}

/* footer */
.footer-bg{left:0;top:4130px;width:1200px;height:514px;background:var(--night-deep)}
.foot-col h4{font-family:var(--body);font-weight:700;font-size:20px;margin-bottom:22px}
.foot-col li{list-style:none;font-size:14px;line-height:21.5px}
.contact-row{display:flex;gap:14px;font-size:14px;line-height:20px;margin-bottom:20px}
.contact-row svg{flex:none;margin-top:3px}
.login-btn{left:164px;top:4403px;width:112px;height:40px;border:2px solid var(--gold);border-radius:30px;display:flex;align-items:center;justify-content:center;font-weight:700;font-size:14px;color:var(--gold)}
.legal{left:112px;top:4577px;font-size:13px}
.pay{top:4570px;width:54px;height:34px;border-radius:4px}
</style>
</head>
<body>
<div class="page">

  <!-- hero artwork -->
  <div class="abs hero-art" role="img" aria-label="Neon metaverse scene: a person in a VR headset gliding on a hoverboard over a glowing wireframe mountain landscape with floating spheres"></div>
  <svg class="abs" style="left:0;top:640px" width="1200" height="170" viewBox="0 0 1200 170" aria-hidden="true">
    <defs>
      <linearGradient id="waveGrad" x1="0" x2="1"><stop offset="0" stop-color="#FFC000"/><stop offset=".5" stop-color="#F0912C"/><stop offset=".75" stop-color="#EB3D1F"/><stop offset="1" stop-color="#E54698"/></linearGradient>
    </defs>
    <path d="M0 100 C 200 20, 420 40, 600 90 S 1000 180, 1200 100 L1200 170 L0 170 Z" fill="#22154a"/>
    <path d="M0 100 C 200 20, 420 40, 600 90 S 1000 180, 1200 100" fill="none" stroke="url(#waveGrad)" stroke-width="5"/>
  </svg>

  <header class="abs site-header">
    <a class="abs brand" style="left:112px;top:32px" href="#"><span class="brand-dot"></span>Quillora</a>
    <span class="abs connect">Connect with us :</span>
    <a class="abs social-circle" style="left:758px;top:36px" href="#" aria-label="Friendloop">Fl</a>
    <a class="abs social-circle" style="left:818px;top:36px" href="#" aria-label="Gathrix">Gx</a>
    <a class="abs social-circle" style="left:876px;top:36px" href="#" aria-label="Scrivo">Sc</a>
    <a class="abs grad-btn header-cta" href="#">Join Waitlist</a>
  </header>

  <h1 class="abs hero-title">Quillora</h1>
  <p class="abs hero-copy">Lorem ipsum dolor sit amet, consectetur adipiscing elit, sed do tempor incididunt ut labore et dolore magna aliqua.</p>
  <a class="abs grad-btn hero-cta" href="#">Join Waitlist</a>
  <div class="abs slider-dots">
    <div class="num">1</div><div class="line"></div>
    <div class="dot" style="top:52px"></div>
    <div class="dot" style="top:87px"></div>
    <div class="dot" style="top:120px"></div>
  </div>

  <!-- featured books -->
  <h2 class="section-title" style="top:852px">Featured Books</h2>

  <!-- row 1 -->
  <div class="abs book-card" style="left:112px;top:1018px"></div>
  <div class="abs book-card" style="left:362px;top:1018px"></div>
  <div class="abs book-card" style="left:612px;top:1018px"></div>
  <div class="abs book-card" style="left:863px;top:1018px"></div>
  <div class="abs book-cover" style="left:146px;top:944px;background:linear-gradient(160deg,#2fa4d8,#e8d23a 60%,#d8392a)" role="img" aria-label="Comic cover: caped superhero flying"></div>
  <div class="abs book-cover" style="left:396px;top:944px;background:linear-gradient(160deg,#f1d13a,#5fb4c8 40%,#b8683a)" role="img" aria-label="Comic cover: barbarian warrior"></div>
  <div class="abs book-cover" style="left:646px;top:944px;background:linear-gradient(160deg,#e8452a,#f4e25a 45%,#4a8ad0)" role="img" aria-label="Comic cover: hero throwing a punch"></div>
  <div class="abs book-cover" style="left:897px;top:944px;background:linear-gradient(160deg,#7a8a2c,#4a5a24 50%,#2a2e18)" role="img" aria-label="Comic cover: tentacled swamp monster"></div>

  <!-- row 2 -->
  <div class="abs book-card" style="left:112px;top:1420px"></div>
  <div class="abs book-card" style="left:362px;top:1420px"></div>
  <div class="abs book-card" style="left:612px;top:1420px"></div>
  <div class="abs book-card" style="left:863px;top:1420px"></div>
  <div class="abs book-cover" style="left:146px;top:1347px;background:linear-gradient(160deg,#3a4a3a,#2b3530 60%,#1e2626)" role="img" aria-label="Comic cover: astronaut and rocket on a dark planet"></div>
  <div class="abs book-cover" style="left:396px;top:1347px;background:linear-gradient(160deg,#3a86d8,#6ac0f0 50%,#e84a2a)" role="img" aria-label="Comic cover: city skyline in blue"></div>
  <div class="abs book-cover" style="left:646px;top:1347px;background:linear-gradient(160deg,#5ab0d8,#e8c05a 50%,#c85a2a)" role="img" aria-label="Comic cover: astronaut in a space capsule"></div>
  <div class="abs book-cover" style="left:897px;top:1347px;background:linear-gradient(160deg,#58c0c0,#e8e8d8 45%,#2a2a2a)" role="img" aria-label="Comic cover: city burst with black towers"></div>

  <!-- authors & buttons row 1 -->
  <div class="abs author" style="left:138px;top:1184px"><div class="author-avatar" role="img" aria-label="Author photo"></div><div><div class="author-name">Hollis Marrow</div><div class="author-role">Nemo enim ipsam</div></div></div>
  <div class="abs author" style="left:388px;top:1184px"><div class="author-avatar" role="img" aria-label="Author photo"></div><div><div class="author-name">Hollis Marrow</div><div class="author-role">Nemo enim ipsam</div></div></div>
  <div class="abs author" style="left:638px;top:1184px"><div class="author-avatar" role="img" aria-label="Author photo"></div><div><div class="author-name">Hollis Marrow</div><div class="author-role">Nemo enim ipsam</div></div></div>
  <div class="abs author" style="left:889px;top:1184px"><div class="author-avatar" role="img" aria-label="Author photo"></div><div><div class="author-name">Hollis Marrow</div><div class="author-role">Nemo enim ipsam</div></div></div>
  <a class="abs buy-btn" style="left:146px;top:1243px" href="#"><span>Inform and Buy</span></a>
  <a class="abs buy-btn" style="left:396px;top:1243px" href="#"><span>Inform and Buy</span></a>
  <a class="abs buy-btn" style="left:646px;top:1243px" href="#"><span>Inform and Buy</span></a>
  <a class="abs buy-btn" style="left:897px;top:1243px" href="#"><span>Inform and Buy</span></a>

  <!-- authors & buttons row 2 -->
  <div class="abs author" style="left:138px;top:1586px"><div class="author-avatar" role="img" aria-label="Author photo"></div><div><div class="author-name">Hollis Marrow</div><div class="author-role">Nemo enim ipsam</div></div></div>
  <div class="abs author" style="left:388px;top:1586px"><div class="author-avatar" role="img" aria-label="Author photo"></div><div><div class="author-name">Hollis Marrow</div><div class="author-role">Nemo enim ipsam</div></div></div>
  <div class="abs author" style="left:638px;top:1586px"><div class="author-avatar" role="img" aria-label="Author photo"></div><div><div class="author-name">Hollis Marrow</div><div class="author-role">Nemo enim ipsam</div></div></div>
  <div class="abs author" style="left:889px;top:1586px"><div class="author-avatar" role="img" aria-label="Author photo"></div><div><div class="author-name">Hollis Marrow</div><div class="author-role">Nemo enim ipsam</div></div></div>
  <a class="abs buy-btn" style="left:146px;top:1645px" href="#"><span>Inform and Buy</span></a>
  <a class="abs buy-btn" style="left:396px;top:1645px" href="#"><span>Inform and Buy</span></a>
  <a class="abs buy-btn" style="left:646px;top:1645px" href="#"><span>Inform and Buy</span></a>
  <a class="abs buy-btn" style="left:897px;top:1645px" href="#"><span>Inform and Buy</span></a>

  <a class="abs grad-btn more-btn" style="left:529px;top:1753px" href="#">View more<i></i></a>

  <!-- team -->
  <h2 class="section-title" style="top:1882px">Our Team</h2>
  <div class="abs member" style="left:154px;top:1971px"><div class="member-photo" style="background:radial-gradient(circle at 50% 45%,#f6d27a 0 30%,#f06b12 31%)" role="img" aria-label="Team member illustration on orange"></div><div class="member-name">John doe</div><div class="member-company">Company name</div></div>
  <div class="abs member" style="left:480px;top:1971px"><div class="member-photo" style="background:radial-gradient(circle at 50% 45%,#e8a070 0 30%,#1f6a5a 31%)" role="img" aria-label="Team member illustration on teal"></div><div class="member-name">John doe</div><div class="member-company">Company name</div></div>
  <div class="abs member" style="left:806px;top:1971px"><div class="member-photo" style="background:radial-gradient(circle at 50% 45%,#e8b08a 0 30%,#f8d21a 31%)" role="img" aria-label="Team member illustration on yellow"></div><div class="member-name">John doe</div><div class="member-company">Company name</div></div>

  <!-- roadmap band -->
  <div class="abs roadmap-band"></div>
  <div class="abs roadmap-glow" role="img" aria-label="Glowing particle wave landscape in purple and blue"></div>
  <svg class="abs" style="left:0;top:2350px" width="1200" height="140" viewBox="0 0 1200 140" aria-hidden="true">
    <defs><linearGradient id="waveGrad2" x1="0" x2="1"><stop offset="0" stop-color="#FFC000"/><stop offset=".5" stop-color="#F0912C"/><stop offset=".75" stop-color="#EB3D1F"/><stop offset="1" stop-color="#E54698"/></linearGradient></defs>
    <path d="M0 68 C 250 -10, 500 30, 700 80 S 1050 140, 1200 60 L1200 0 L0 0 Z" fill="#22154a"/>
    <path d="M0 68 C 250 -10, 500 30, 700 80 S 1050 140, 1200 60" fill="none" stroke="url(#waveGrad2)" stroke-width="5"/>
  </svg>
  <svg class="abs" style="left:0;top:3120px" width="1200" height="110" viewBox="0 0 1200 110" aria-hidden="true">
    <defs><linearGradient id="waveGrad3" x1="0" x2="1"><stop offset="0" stop-color="#FFC000"/><stop offset=".5" stop-color="#F0912C"/><stop offset=".75" stop-color="#EB3D1F"/><stop offset="1" stop-color="#E54698"/></linearGradient></defs>
    <path d="M0 35 C 200 90, 450 90, 650 50 S 1000 -10, 1200 40 L1200 110 L0 110 Z" fill="#22154a"/>
    <path d="M0 35 C 200 90, 450 90, 650 50 S 1000 -10, 1200 40" fill="none" stroke="url(#waveGrad3)" stroke-width="5"/>
  </svg>

  <h2 class="section-title" style="top:2538px">Road map</h2>

  <div class="abs stage" style="left:112px;background:var(--gold)"><div class="stage-icon" style="border-color:var(--gold)"><svg width="40" height="40" viewBox="0 0 40 40" fill="none" stroke="#333" stroke-width="1.6"><circle cx="20" cy="20" r="4"/><circle cx="8" cy="8" r="3"/><circle cx="32" cy="8" r="3"/><circle cx="8" cy="32" r="3"/><circle cx="32" cy="32" r="3"/><path d="M10 10l7 7M30 10l-7 7M10 30l7-7M30 30l-7-7"/></svg></div><span class="stage-label">Nemo enimip</span></div>
  <div class="abs stage" style="left:355px;background:#e8101a"><div class="stage-icon" style="border-color:#e8101a"><svg width="40" height="40" viewBox="0 0 40 40" fill="none" stroke="#333" stroke-width="1.6"><rect x="14" y="14" width="12" height="12"/><rect x="4" y="4" width="8" height="8"/><rect x="28" y="28" width="8" height="8"/><path d="M12 8h10v6M28 32H18v-6"/></svg></div><span class="stage-label">Nemo enimip</span></div>
  <div class="abs stage" style="left:598px;background:var(--grey)"><div class="stage-icon" style="border-color:var(--grey)"><svg width="40" height="40" viewBox="0 0 40 40" fill="none" stroke="#333" stroke-width="1.6"><rect x="10" y="16" width="20" height="16" rx="2"/><path d="M14 16v-4a6 6 0 0 1 12 0v4"/><circle cx="20" cy="24" r="2"/></svg></div><span class="stage-label">Nemo enimip</span></div>
  <div class="abs stage" style="left:841px;width:247px;background:var(--blue)"><div class="stage-icon" style="border-color:var(--blue)"><svg width="40" height="40" viewBox="0 0 40 40" fill="none" stroke="#333" stroke-width="1.6"><path d="M20 4l14 8v16l-14 8-14-8V12z"/><text x="20" y="24" font-size="9" text-anchor="middle" fill="#333" stroke="none" font-family="Arimo,sans-serif">NFT</text></svg></div><span class="stage-label">Nemo enimip</span></div>

  <span class="abs milestone-no" style="left:148px;top:2638px">01</span>
  <div class="abs milestone-line" style="left:155px;top:2656px;height:110px;background:var(--gold)"></div>
  <p class="abs milestone-text" style="left:176px;top:2660px">Lorem ipsum dolor sit amet, consectetur adipiscing elit, sed do eiusmod tempor incididunt ut labore et dolore</p>

  <span class="abs milestone-no" style="left:624px;top:2638px">03</span>
  <div class="abs milestone-line" style="left:630px;top:2656px;height:110px;background:var(--grey)"></div>
  <p class="abs milestone-text" style="left:654px;top:2660px">Lorem ipsum dolor sit amet, consectetur adipiscing elit, sed do eiusmod tempor incididunt ut labore et dolore</p>

  <div class="abs milestone-line" style="left:393px;top:2852px;height:112px;background:#e8101a"></div>
  <span class="abs milestone-no" style="left:386px;top:2966px">02</span>
  <p class="abs milestone-text" style="left:414px;top:2876px">Lorem ipsum dolor sit amet, consectetur adipiscing elit, sed do eiusmod tempor incididunt ut labore et dolore</p>

  <div class="abs milestone-line" style="left:870px;top:2852px;height:112px;background:var(--blue)"></div>
  <span class="abs milestone-no" style="left:863px;top:2966px">04</span>
  <p class="abs milestone-text" style="left:892px;top:2876px">Lorem ipsum dolor sit amet, consectetur adipiscing elit, sed do eiusmod tempor incididunt ut labore et dolore</p>

  <!-- white papers -->
  <h2 class="section-title" style="top:3242px">White Papers</h2>
  <article class="abs paper-card" style="left:110px"><div class="paper-mesh" role="img" aria-label="Grey wireframe grid landscape"></div><h3>Nemo enim ipsam</h3><p>Lorem ipsum dolor sit amet, consectetur adipiscing elit, sed do eiusmod tempor incididunt ut labore</p><a class="learn" href="#">Learn more ➜</a></article>
  <article class="abs paper-card" style="left:444px"><div class="paper-mesh" role="img" aria-label="Grey wireframe grid landscape"></div><h3>Nemo enim ipsam</h3><p>Lorem ipsum dolor sit amet, consectetur adipiscing elit, sed do eiusmod tempor incididunt ut labore</p><a class="learn" href="#">Learn more ➜</a></article>
  <article class="abs paper-card" style="left:777px"><div class="paper-mesh" role="img" aria-label="Grey wireframe grid landscape"></div><h3>Nemo enim ipsam</h3><p>Lorem ipsum dolor sit amet, consectetur adipiscing elit, sed do eiusmod tempor incididunt ut labore</p><a class="learn" href="#">Learn more ➜</a></article>

  <a class="abs grad-btn more-btn" style="left:529px;top:3683px" href="#">View more<i></i></a>

  <!-- newsletter -->
  <section class="abs newsletter">
    <h2>Suscribe<br>Our Newsletter</h2>
    <div class="signup">Email address<span class="signup-btn">SUBSCRIBE NOW</span></div>
  </section>

  <!-- footer -->
  <div class="abs footer-bg"></div>
  <svg class="abs" style="left:0;top:4100px" width="1200" height="120" viewBox="0 0 1200 120" aria-hidden="true">
    <defs><linearGradient id="waveGrad4" x1="0" x2="1"><stop offset="0" stop-color="#EB3D1F"/><stop offset=".5" stop-color="#E54698"/><stop offset="1" stop-color="#EB3D1F"/></linearGradient></defs>
    <path d="M0 70 C 250 10, 450 20, 650 60 S 1000 90, 1200 20 L1200 0 L0 0 Z" fill="#22154a"/>
    <path d="M0 70 C 250 10, 450 20, 650 60 S 1000 90, 1200 20" fill="none" stroke="url(#waveGrad4)" stroke-width="4"/>
  </svg>

  <a class="abs brand" style="left:112px;top:4334px" href="#"><span class="brand-dot"></span>Quillora</a>
  <a class="abs login-btn" href="#">LOGIN</a>

  <div class="abs foot-col" style="left:404px;top:4305px">
    <h4>Quick Links</h4>
    <ul><li>Home</li><li>About us</li><li>Project</li><li>Testimonials</li><li>Blog</li><li>FAQ</li></ul>
  </div>
  <div class="abs foot-col" style="left:641px;top:4305px;width:260px">
    <h4>Contact us</h4>
    <div class="contact-row"><svg width="11" height="14" viewBox="0 0 11 14"><path d="M5.5 0A5.5 5.5 0 0 0 0 5.5C0 9.6 5.5 14 5.5 14S11 9.6 11 5.5A5.5 5.5 0 0 0 5.5 0zm0 7.5a2 2 0 1 1 0-4 2 2 0 0 1 0 4z" fill="#E54698"/></svg><span>Sed ut perspiciatis unde omnis iste natus error</span></div>
    <div class="contact-row"><svg width="12" height="12" viewBox="0 0 12 12"><path d="M2.4 0l2 2.8-1.2 1.4a7 7 0 0 0 4.6 4.6L9.2 7.6 12 9.6 10.6 12C4.8 12 0 7.2 0 1.4z" fill="#E54698"/></svg><span>+1 888 888 8888</span></div>
    <div class="contact-row"><svg width="13" height="10" viewBox="0 0 13 10"><rect width="13" height="10" rx="1" fill="#E54698"/><path d="M0 1l6.5 5L13 1" stroke="#150b30" fill="none"/></svg><span>info@companyname.com</span></div>
  </div>
  <div class="abs foot-col" style="left:944px;top:4305px">
    <h4>Follow us</h4>
    <ul><li>Friendloop</li><li>Chirpna</li><li>Proflink</li><li>Snapgrid</li><li>Vidstream</li></ul>
  </div>

  <p class="abs legal">Copyright &nbsp;© 2022 Company name | Privacy Policy | Terms &amp; Conditions</p>
  <div class="abs pay" style="left:685px;background:#2b4fa8" aria-label="Card payment"></div>
  <div class="abs pay" style="left:752px;background:#e8e8e8" aria-label="Card payment"></div>
  <div class="abs pay" style="left:819px;background:#2d7fd0" aria-label="Card payment"></div>
  <div class="abs pay" style="left:886px;background:#dfe6f2" aria-label="Online payment"></div>
  <div class="abs pay" style="left:953px;background:#f29a2e" aria-label="Card payment"></div>
  <div class="abs pay" style="left:1020px;background:#2a2a2a" aria-label="Money transfer"></div>

</div>
</body>
</html>
```